rhyming dictionary website (easy)

i need a web design for my new website which for now runs on my own self made design (i am a programmer so it sucks) you can find it at http://www.tallow-grove.com

i would like a nicer design that will not cause visitors to flee in disgust.

Target Market(s)

people who search for rhymes, poets, rappers, and normal birthday greeting people

Requirements
Must have
• this is what it needs to have:

1. main page which is simple and must emphasize on the search bar.

2. search result page that will emphasize on the rhyming words and make them clear and important, it also needs to be separable like in the current "design".
it also need to have a good placement of ads, not too intrusive, not too unnoticeable

3. a general page with no real content that i can fill with anything later.
Nice to have
• also the design could combine the already exist logo that you can see on the website, i added it in the uploaded files, along with its psd.

p.s:
other design i liked that you can inspire yourself from
http://www.quillbox.net/RhymingDictionary/hello.html

```html
<!DOCTYPE html>
<html lang="en">
<head>
<meta charset="utf-8">
<title>Tallow Grove – your source for rhymes online</title>
<link href="https://fonts.googleapis.com/css2?family=Josefin+Sans:wght@600;700&family=Open+Sans:ital,wght@0,300;0,400;0,700;1,400&display=swap" rel="stylesheet">
<style>
  :root {
    --taupe: #958777;
    --green: #72c05e;
    --green-dark: #0f8a00;
    --sky: #6acde6;
    --sky-dark: #04a2ce;
    --indigo: #36479b;
    --indigo-dark: #020444;
    --berry: #b01c52;
    --berry-dark: #7a0000;
    --text-berry: #9b2150;
    --grey-text: #8a8a8a;
    --footer: #333333;
    --footer-text: #9a9a9a;
    --white: #ffffff;
    --photo-deep: #0b1f3a;
    --photo-mid: #1a5e9e;
    --photo-light: #3fa0d8;
  }
  * { box-sizing: border-box; margin: 0; padding: 0; }
  html, body { width: 1113px; height: 1200px; overflow: hidden; background: var(--white); }
  body { position: relative; font-family: "Open Sans", Arial, sans-serif; }

  .top-strip { position: absolute; left: 0; top: 0; width: 458px; height: 20px; background: var(--taupe); }

  .brand { position: absolute; left: 0; top: 20px; width: 458px; height: 176px; background: var(--white); }
  .brand__mark { position: absolute; left: 49px; top: 54px; width: 24px; height: 24px; background: var(--berry); }
  .brand__name { position: absolute; left: 84px; top: 40px; font-size: 40px; font-weight: 300; color: var(--grey-text); letter-spacing: -0.5px; }
  .brand__tagline { position: absolute; left: 50px; top: 117px; font-size: 15px; color: var(--grey-text); }
  .account-links { position: absolute; left: 331px; top: 12px; font-size: 12px; color: var(--grey-text); }
  .account-links span { margin: 0 6px; }

  .main-nav { position: absolute; left: 458px; top: 0; width: 655px; height: 196px; display: flex; }
  .main-nav__item { flex: 1; display: flex; align-items: center; justify-content: center;
    font-family: "Josefin Sans", sans-serif; font-weight: 700; font-size: 17px; color: var(--white);
    letter-spacing: 1px; text-transform: uppercase; padding-top: 14px; border-top: 20px solid; }
  .main-nav__item--home { background: var(--green); border-color: var(--green-dark); }
  .main-nav__item--about { background: var(--sky); border-color: var(--sky-dark); }
  .main-nav__item--how { background: var(--indigo); border-color: var(--indigo-dark); }
  .main-nav__item--contact { background: var(--berry); border-color: var(--berry-dark); }

  .hero-visual { position: absolute; left: 0; top: 196px; width: 453px; height: 260px;
    background: radial-gradient(ellipse at 55% 40%, var(--photo-light), var(--photo-mid) 45%, var(--photo-deep)); }

  .intro { position: absolute; left: 502px; top: 233px; width: 560px; font-size: 15px; line-height: 27px; color: var(--text-berry); }

  .search { position: absolute; left: 500px; top: 364px; width: 577px; height: 46px;
    border: 1px solid #8c8c8c; border-radius: 23px; background: var(--white); }
  .search__field { position: absolute; left: 23px; top: 12px; font-size: 15px; font-style: italic; color: #6b6fa8; }
  .search__button { position: absolute; right: -1px; top: -1px; width: 220px; height: 46px; border-radius: 23px;
    background: linear-gradient(#6a78c9, #3a4aa3 55%, #34449b); border: 1px solid #2c3a86;
    color: var(--white); font-weight: 700; font-size: 20px; display: flex; align-items: center; justify-content: center; }

  .latest { position: absolute; left: 0; top: 460px; width: 453px; height: 546px; background: var(--taupe); color: var(--white); }
  .latest__title { position: absolute; left: 50px; top: 40px; font-family: "Josefin Sans", sans-serif; font-weight: 700;
    font-size: 21px; letter-spacing: 1px; text-transform: uppercase; }
  .latest__list { position: absolute; left: 52px; top: 95px; list-style: none; font-size: 15px; line-height: 27.3px; }
  .latest__list--second { top: 237px; }
  .latest__more { position: absolute; left: 50px; top: 394px; font-size: 15px; font-weight: 700; }

  .feature-visual { position: absolute; left: 458px; top: 460px; width: 655px; height: 546px;
    background: radial-gradient(ellipse at 60% 35%, var(--photo-light), var(--photo-mid) 45%, var(--photo-deep)); }

  .footer-nav { position: absolute; left: 0; top: 1011px; width: 1113px; height: 44px; display: flex; gap: 6px; }
  .footer-nav__item { flex: 1; display: flex; align-items: center; justify-content: center; color: var(--white);
    font-family: "Josefin Sans", sans-serif; font-weight: 700; font-size: 16px; letter-spacing: 1px; text-transform: uppercase; padding-top: 3px; }

  .site-footer { position: absolute; left: 0; top: 1060px; width: 1113px; height: 140px; background: var(--footer);
    font-size: 12.5px; line-height: 20.5px; color: var(--footer-text); }
  .site-footer__col { position: absolute; top: 22px; }
  .site-footer__col--rights { left: 59px; }
  .site-footer__col--address { left: 456px; }
  .site-footer__col--legal { left: 863px; }
</style>
</head>
<body>
  <div class="top-strip"></div>

  <header class="brand">
    <div class="brand__mark"></div>
    <div class="brand__name">Tallow Grove</div>
    <div class="brand__tagline">your source for rhymes online</div>
    <div class="account-links">Sign Up<span>|</span>Register</div>
  </header>

  <nav class="main-nav">
    <div class="main-nav__item main-nav__item--home">Home</div>
    <div class="main-nav__item main-nav__item--about">About Us</div>
    <div class="main-nav__item main-nav__item--how">How It Works</div>
    <div class="main-nav__item main-nav__item--contact">Contact</div>
  </nav>

  <div class="hero-visual" role="img" aria-label="Blue 3D scene of glass human figures standing on a digital city grid"></div>

  <p class="intro">So you're writing a song or a poem and are frustrated from searching for the right rhyme? Then you're in the right place!<br>Our automated system will fix you the perfect rhyme, that will make you look like the poet you always wanted to be.</p>

  <div class="search">
    <span class="search__field">Search...</span>
    <div class="search__button">NOW</div>
  </div>

  <section class="latest">
    <h2 class="latest__title">Latest Searches</h2>
    <ul class="latest__list">
      <li>hello</li><li>sex</li><li>dead</li><li>more</li><li>throne</li>
    </ul>
    <ul class="latest__list latest__list--second">
      <li>hello</li><li>sex</li><li>dead</li><li>more</li><li>throne</li>
    </ul>
    <div class="latest__more">Read more</div>
  </section>

  <div class="feature-visual" role="img" aria-label="Blue 3D scene of glass human figures with glowing DNA base labels guanine and cytosine"></div>

  <nav class="footer-nav">
    <div class="footer-nav__item" style="background: var(--green)">Home</div>
    <div class="footer-nav__item" style="background: var(--sky)">About Us</div>
    <div class="footer-nav__item" style="background: var(--indigo)">How It Works</div>
    <div class="footer-nav__item" style="background: var(--berry)">Contact</div>
  </nav>

  <footer class="site-footer">
    <div class="site-footer__col site-footer__col--rights">All rights are allright<br>They are reserved as they well deserved.</div>
    <div class="site-footer__col site-footer__col--address">Address<br>1170 Marrow Lane<br>Ashford Hills, MI 48012</div>
    <div class="site-footer__col site-footer__col--legal">Privacy Policy<br>Terms &amp; Conditions<br>Contact Us</div>
  </footer>
</body>
</html>
```